Cutting edge GUI for a conventional C# Forms Project

I have an existing C# Forms application. The current GUI design format is Win 95 style forms. I would like to elevate the look of the software.

There are a total of six forms. Apart from two forms at 1024 X 600, the others are of different sizes. I am open to resizing them depending on the design.

I am attaching the user manual of the product to give you a better idea of what the application does. The manual also contains screenshots of individual screens. I am open to sharing the C# source files if needed.

Target Market(s)

Industrial application - Field Representatives - Will be used in Outdoor environments.

Industry/Entity Type

Software

Requirements
Must have
• A very cool, futuristic design.
Design should be light-weight as the application maybe run on net-books and low end tablets.
Should not have
• Redundant point but keep in mind that this design is going to be used in a software. So light weight is highly appreciated.

```html
<!DOCTYPE html>
<html lang="en">
<head>
<meta charset="utf-8">
<title>NV Calliper – Run Records</title>
<link href="https://fonts.googleapis.com/css2?family=Aleo:wght@300;400&family=Lato:ital,wght@0,300;0,400;1,300&display=swap" rel="stylesheet">
<style>
  :root {
    --page-bg: #f1f1f1;
    --sky: #80cfee;
    --sky-soft: #d6edf8;
    --sky-footer: #a8dcf2;
    --white: #ffffff;
    --ink: #444b4f;
    --ink-soft: #8a8f93;
    --table-head: #2f8fcf;
    --rule: #d4d6d8;
  }
  * { box-sizing: border-box; margin: 0; padding: 0; }
  html, body {
    width: 1200px; height: 673px; overflow: hidden;
    background: var(--page-bg);
    font-family: "Aleo", Georgia, serif;
  }
  .stage {
    position: relative; width: 1358px; height: 762px;
    transform: scale(0.88365); transform-origin: 0 0;
  }
  .top-strip {
    position: absolute; left: 0; top: 0; width: 1290px; height: 8px;
    background: var(--white); box-shadow: 0 1px 2px rgba(0,0,0,.08);
  }
  .window {
    position: absolute; left: 87px; top: 30px; width: 1144px; height: 687px;
    background: var(--white);
  }
  .title-bar {
    position: absolute; left: 0; top: 0; width: 100%; height: 46px;
    background: var(--sky);
  }
  .title-bar h1 {
    position: absolute; left: 65px; top: 3px;
    font-weight: 400; font-size: 34px; color: var(--white); letter-spacing: .3px;
  }
  .window-controls { position: absolute; right: 18px; top: 13px; }
  .window-controls svg { display: block; }

  .header-panel {
    position: absolute; left: 0; top: 46px; width: 100%; height: 217px;
    background: var(--sky-soft);
  }
  .job-photo {
    position: absolute; left: 10px; top: 16px; width: 169px; height: 168px;
    border: 4px solid var(--white); background: var(--sky-soft);
  }
  .job-info {
    position: absolute; left: 240px; top: 16px;
    display: grid; grid-template-columns: 155px auto; column-gap: 20px;
    row-gap: 6.6px; font-size: 17px; line-height: 22px;
  }
  .job-info dt { text-align: right; color: var(--ink); }
  .job-info dd { color: var(--ink-soft); font-weight: 300; }

  .scroll-btn {
    position: absolute; left: 568px; width: 80px; height: 80px;
    border: 4px solid var(--white); display: flex; align-items: center; justify-content: center;
  }
  .scroll-btn.up { top: 14px; }
  .scroll-btn.down { top: 104px; opacity: .55; }

  .action-btn {
    position: absolute; left: 768px; width: 298px; height: 82px;
    border: 4px solid var(--white); background: var(--sky-soft);
    display: flex; align-items: center; justify-content: center;
    font-family: "Aleo", Georgia, serif; font-size: 24px; color: var(--ink);
  }
  .action-btn.menu { top: 15px; }
  .action-btn.report { top: 105px; }
  .header-rule {
    position: absolute; left: 10px; top: 193px; width: 1118px; height: 3px; background: var(--white);
  }

  .records {
    position: absolute; left: 11px; top: 263px; width: 1138px;
    font-family: "Lato", Arial, sans-serif;
  }
  .records-head, .record-row { position: relative; height: 50px; }
  .records-head {
    height: 62px; border-bottom: 1.5px solid var(--rule);
    color: var(--table-head); font-size: 21px; font-weight: 300;
  }
  .records-head span, .record-row span {
    position: absolute; transform: translateX(-50%); white-space: nowrap;
  }
  .records-head span { top: 15px; }
  .record-row { color: #6e7377; font-size: 17px; font-style: italic; font-weight: 300; }
  .record-row:first-of-type { margin-top: 6px; }
  .record-row span { top: 8px; }
  .c-serial { left: 53px; } .c-time { left: 194px; } .c-dist { left: 349px; }
  .c-min { left: 492px; } .c-clock { left: 629px; } .c-len { left: 761px; }
  .c-prog { left: 909px; }
  .bar {
    position: absolute; left: 839px; top: 7px; width: 201px; height: 21px;
    border: 2px solid var(--sky); background: var(--white);
  }
  .bar i { display: block; height: 100%; background: var(--sky); }
  .record-row .pct { left: 1072px; top: 5px; font-size: 16px; transform: none; }

  .status-bar {
    position: absolute; left: 0; bottom: 0; width: 100%; height: 47px;
    background: var(--sky-footer); font-size: 15px; color: var(--ink);
  }
  .units { position: absolute; left: 17px; top: 15px; }
  .units-stepper { position: absolute; left: 131px; top: 2px; }
  .download-label { position: absolute; left: 717px; top: 15px; }
  .download-bar {
    position: absolute; left: 914px; top: 13px; width: 200px; height: 21px;
    border: 2px solid var(--white); background: var(--white);
  }
  .download-bar i { position: absolute; right: 0; top: 0; height: 100%; width: 38%; background: var(--sky-footer); }
</style>
</head>
<body>
<div class="stage">
  <div class="top-strip"></div>
  <main class="window">
    <header class="title-bar">
      <h1>NV Calliper</h1>
      <div class="window-controls">
        <svg width="72" height="22" viewBox="0 0 72 22" aria-hidden="true">
          <rect x="0" y="10" width="18" height="5" fill="#fff"/>
          <path d="M53 3 L69 19 M69 3 L53 19" stroke="#fff" stroke-width="4.5" stroke-linecap="round"/>
        </svg>
      </div>
    </header>

    <section class="header-panel">
      <div class="job-photo" role="img" aria-label="Tool photo"></div>
      <dl class="job-info">
        <dt>Job Number</dt><dd>A1234</dd>
        <dt>Run Type</dt><dd>Lorem Ipsum</dd>
        <dt>Distance</dt><dd>5.26</dd>
        <dt>Tool Size</dt><dd>6.2</dd>
        <dt>Tool ON Time</dt><dd>06:20:30</dd>
        <dt>Download Time</dt><dd>00:12:34</dd>
      </dl>
      <div class="scroll-btn up">
        <svg width="42" height="34" viewBox="0 0 42 34" aria-hidden="true"><path d="M21 0 L42 34 H0 Z" fill="#fff"/></svg>
      </div>
      <div class="scroll-btn down">
        <svg width="42" height="34" viewBox="0 0 42 34" aria-hidden="true"><path d="M0 0 H42 L21 34 Z" fill="#fff"/></svg>
      </div>
      <button class="action-btn menu">Back to Main Menu</button>
      <button class="action-btn report">Create Report</button>
      <div class="header-rule"></div>
    </section>

    <section class="records">
      <div class="records-head">
        <span class="c-serial">Serial</span><span class="c-time">Time</span>
        <span class="c-dist">Distance</span><span class="c-min">Min ID</span>
        <span class="c-clock">O’ Clock</span><span class="c-len">Length</span>
        <span class="c-prog">Progress</span>
      </div>
      <div class="record-row">
        <span class="c-serial">01</span><span class="c-time">10-12-2013- 08:56</span>
        <span class="c-dist">20</span><span class="c-min">20</span><span class="c-clock">20</span><span class="c-len">20</span>
        <div class="bar"><i style="width:61%"></i></div><span class="pct">61%</span>
      </div>
      <div class="record-row">
        <span class="c-serial">02</span><span class="c-time">11-12-2013- 10:12</span>
        <span class="c-dist">40</span><span class="c-min">40</span><span class="c-clock">40</span><span class="c-len">40</span>
        <div class="bar"><i style="width:18%"></i></div><span class="pct">18%</span>
      </div>
      <div class="record-row">
        <span class="c-serial">03</span><span class="c-time">10-12-2013- 08:56</span>
        <span class="c-dist">20</span><span class="c-min">20</span><span class="c-clock">20</span><span class="c-len">20</span>
        <div class="bar"><i style="width:95%"></i></div><span class="pct">95%</span>
      </div>
      <div class="record-row">
        <span class="c-serial">04</span><span class="c-time">11-12-2013- 10:12</span>
        <span class="c-dist">40</span><span class="c-min">40</span><span class="c-clock">40</span><span class="c-len">40</span>
        <div class="bar"><i style="width:81%"></i></div><span class="pct">83%</span>
      </div>
    </section>

    <footer class="status-bar">
      <span class="units">Units : Metric</span>
      <svg class="units-stepper" width="20" height="43" viewBox="0 0 20 43" aria-hidden="true">
        <rect x="1" y="1" width="18" height="19" fill="none" stroke="#fff" stroke-width="1.5"/>
        <rect x="1" y="23" width="18" height="19" fill="none" stroke="#fff" stroke-width="1.5"/>
        <path d="M10 6 L15 14 H5 Z M5 28 H15 L10 36 Z" fill="#fff"/>
      </svg>
      <span class="download-label">Downloading Records 2/3</span>
      <div class="download-bar"><i></i></div>
    </footer>
  </main>
</div>
</body>
</html>
```